WANTED: The Best Mobile App Designers

We are looking for the best mobile app designers.

This is a small test job to test your skills and the winner will be given ongoing work which means ongoing work and revenue for you!

If you do not feel you are the BEST please DO NOT APPLY as we are only looking for "the" best mobile app designers with experience.

Attached is a test spec for a design we need.

Look forward to seeing your skills and creating a long term relationship.

Target Market(s)

General consumers who are looking to sell their unwanted items to make extra cash

Industry/Entity Type

Work

Requirements
Must have
• The designs must match and look great with the attached logo.

Design must be top quality and give the impression of a billion dollar company.

```html
<!DOCTYPE html>
<html lang="en">
<head>
<meta charset="utf-8">
<title>Keltor5 Listing Screen</title>
<link href="https://fonts.googleapis.com/css2?family=Roboto:wght@400;500&family=Roboto+Condensed:wght@700&family=Signika:wght@600&display=swap" rel="stylesheet">
<style>
  :root {
    --page-bg: #f1f2f4;
    --screen-bg: #eceef0;
    --header-blue: #2b78db;
    --header-blue-dark: #1f63c0;
    --icon-blue: #2a72d5;
    --card-white: #ffffff;
    --card-border: #d6d9dc;
    --label-grey: #5a5d60;
    --offer-yellow: #fdbf10;
    --offer-text: #1d1d1d;
    --price-red: #e0161b;
    --buy-green-top: #94c652;
    --buy-green-bottom: #66a030;
    --thumb-light: #8fb25a;
    --thumb-dark: #3f6a22;
  }
  * { box-sizing: border-box; margin: 0; padding: 0; }
  html, body { width: 1200px; height: 2260px; overflow: hidden; }
  body { background: var(--page-bg); font-family: "Roboto", Arial, sans-serif; position: relative; }

  .app-screen {
    position: absolute; left: 0; top: 230px; width: 1200px; height: 1800px;
    background: var(--screen-bg); overflow: hidden;
  }

  .top-bar {
    position: absolute; left: 0; top: 0; width: 1200px; height: 160px;
    background: linear-gradient(var(--header-blue), var(--header-blue-dark));
    color: #fff;
  }
  .top-bar .back { position: absolute; left: 36px; top: 45px; width: 70px; height: 70px; }
  .top-bar .title {
    position: absolute; left: 140px; top: 0; width: 915px; line-height: 160px;
    font-size: 68px; font-weight: 500; white-space: nowrap; overflow: hidden;
  }
  .top-bar .search {
    position: absolute; right: 0; top: 0; width: 125px; height: 160px;
    border-left: 3px solid rgba(255,255,255,.35); background: var(--header-blue);
    display: flex; align-items: center; justify-content: center;
  }

  .gallery-card {
    position: absolute; left: 21px; top: 195px; width: 1157px; height: 1100px;
    background: var(--card-white); border: 2px solid var(--card-border);
  }
  .thumb {
    position: absolute; left: 22px; width: 165px; height: 165px;
    background: linear-gradient(135deg, var(--thumb-light), var(--thumb-dark));
    border: 3px solid #fff; outline: 2px solid #cfd3d6;
  }
  .thumb.t1 { top: 22px; } .thumb.t2 { top: 200px; } .thumb.t3 { top: 376px; }
  .thumb.t4 { top: 558px; } .thumb.t5 { top: 742px; }
  .play-button {
    position: absolute; left: 22px; top: 922px; width: 165px; height: 165px;
    background: var(--icon-blue); border: 4px solid #1a55a8;
    display: flex; align-items: center; justify-content: center;
  }
  .main-photo {
    position: absolute; left: 208px; top: 22px; width: 920px; height: 1065px;
    background:
      radial-gradient(ellipse at 55% 12%, #f59a2a 0%, #c8631c 35%, transparent 70%),
      linear-gradient(#b5702e 0%, #6d4a2e 45%, #8a5430 75%, #5a3418 100%);
  }
  .price-tag {
    position: absolute; right: 0; bottom: 42px; width: 318px; height: 124px;
    background: var(--price-red);
    clip-path: polygon(0 0, 100% 0, 100% 100%, 0 100%, 9% 50%);
    color: #fff; font-family: "Roboto Condensed", Arial, sans-serif; font-weight: 700;
    font-size: 88px; line-height: 124px; text-align: center; padding-left: 30px;
  }

  .action-bar {
    position: absolute; left: 21px; top: 1335px; width: 1151px; height: 200px;
    background: var(--card-white); border: 2px solid var(--card-border); overflow: hidden;
  }
  .action {
    position: absolute; top: 28px; width: 220px; text-align: center;
    color: var(--label-grey); font-size: 46px; line-height: 56px;
  }
  .action svg { display: block; height: 78px; width: auto; margin: 0 auto 14px; }
  .action.watch { left: 30px; } .action.share { left: 266px; } .action.distance { left: 502px; }
  .make-offer {
    position: absolute; right: 0; top: 0; width: 416px; height: 196px;
    background: var(--offer-yellow); border-radius: 120px 0 0 120px / 98px 0 0 98px;
    font-family: "Roboto Condensed", Arial, sans-serif; font-weight: 700;
    font-size: 74px; color: var(--offer-text); line-height: 196px; text-align: center;
    padding-left: 30px; white-space: nowrap;
  }

  .buy-now {
    position: absolute; left: 21px; top: 1566px; width: 1151px; height: 190px;
    background: linear-gradient(var(--buy-green-top), var(--buy-green-bottom));
    border: 2px solid #5a8d2a; border-radius: 8px; box-shadow: 0 6px 8px rgba(0,0,0,.25);
    font-family: "Signika", Arial, sans-serif; font-weight: 600; font-size: 108px;
    color: #fff; text-align: center; line-height: 186px;
    text-shadow: 0 3px 3px rgba(0,0,0,.25);
  }
</style>
</head>
<body>
  <main class="app-screen">
    <header class="top-bar">
      <svg class="back" viewBox="0 0 70 70"><polyline points="44,14 24,35 44,56" fill="none" stroke="#fff" stroke-width="8" stroke-linecap="round" stroke-linejoin="round"/></svg>
      <h1 class="title">Keltor5 Lorem ipsum met</h1>
      <div class="search">
        <svg width="72" height="72" viewBox="0 0 72 72"><circle cx="28" cy="28" r="18" fill="none" stroke="#fff" stroke-width="8"/><line x1="41" y1="41" x2="62" y2="62" stroke="#fff" stroke-width="10" stroke-linecap="round"/></svg>
      </div>
    </header>

    <section class="gallery-card">
      <div class="thumb t1" role="img" aria-label="Product thumbnail photo"></div>
      <div class="thumb t2" role="img" aria-label="Product thumbnail photo"></div>
      <div class="thumb t3" role="img" aria-label="Product thumbnail photo"></div>
      <div class="thumb t4" role="img" aria-label="Product thumbnail photo"></div>
      <div class="thumb t5" role="img" aria-label="Product thumbnail photo"></div>
      <div class="play-button">
        <svg width="90" height="100" viewBox="0 0 90 100"><polygon points="12,8 82,50 12,92" fill="#fff"/></svg>
      </div>
      <div class="main-photo" role="img" aria-label="Photo of two smartphones lying on a wooden table with warm blurred background">
        <div class="price-tag">$250</div>
      </div>
    </section>

    <nav class="action-bar">
      <div class="action watch">
        <svg viewBox="0 0 76 76"><path d="M38 70 C10 48 2 36 2 22 C2 11 11 4 21 4 C29 4 35 9 38 15 C41 9 47 4 55 4 C65 4 74 11 74 22 C74 36 66 48 38 70 Z" fill="var(--icon-blue)"/></svg>
        Watch
      </div>
      <div class="action share">
        <svg viewBox="0 0 76 76"><line x1="16" y1="38" x2="58" y2="14" stroke="var(--icon-blue)" stroke-width="5"/><line x1="16" y1="38" x2="58" y2="62" stroke="var(--icon-blue)" stroke-width="5"/><circle cx="16" cy="38" r="11" fill="var(--icon-blue)"/><circle cx="58" cy="14" r="11" fill="var(--icon-blue)"/><circle cx="58" cy="62" r="11" fill="var(--icon-blue)"/></svg>
        Share
      </div>
      <div class="action distance">
        <svg viewBox="0 0 56 80"><path d="M28 78 C22 62 2 44 2 26 C2 11 14 2 28 2 C42 2 54 11 54 26 C54 44 34 62 28 78 Z" fill="var(--icon-blue)"/><circle cx="28" cy="26" r="9" fill="#fff"/></svg>
        3 km
      </div>
      <div class="make-offer">Make Offer</div>
    </nav>

    <div class="buy-now">Buy Now!</div>
  </main>
</body>
</html>
```